Website for Excavator and Earthworks Company

We require a modern, sleek and practical website for our newly created earthworks/excavator business in Perth, Western Australia called Gullwind Stonecut Earthworks.

The website should have a modern, cutting edge feel but only needs to be relatively simplistic in it's layout and eventual functionality.

Some pages it should have would be Home, About, Projects and Contact Us.

Number of Pages Required

1 page

```html
<!DOCTYPE html>
<html lang="en">
<head>
<meta charset="utf-8">
<title>Gullwind Stonecut Earthworks</title>
<link rel="stylesheet" href="https://fonts.googleapis.com/css2?family=Archivo+Black&family=Montserrat:wght@400;500;600;700&family=Oswald:wght@500&display=swap">
<style>
:root{
  --bg:#232323;
  --bg-deep:#151515;
  --footer:#2b2b2b;
  --lime:#c5d800;
  --lime-soft:#e6ec99;
  --ink:#1a1a1a;
  --white:#ffffff;
  --muted:#cfcfcf;
  --photo-a:#5f6a5a;
  --photo-b:#e0a21c;
  --blue:#2e6aa6;
}
*{box-sizing:border-box;margin:0;padding:0}
html,body{width:1200px;height:3858px;overflow:hidden}
body{background:var(--bg);color:var(--white);font-family:"Montserrat",sans-serif;position:relative}
.abs{position:absolute}
.display{font-family:"Archivo Black",sans-serif;line-height:1.08}
.btn{position:absolute;display:flex;align-items:center;justify-content:center;font-weight:700;font-size:15px;text-transform:uppercase;border-radius:4px}
.btn-lime{background:var(--lime);color:var(--ink)}
.btn-outline{border:1.5px solid var(--white);color:var(--white)}
.btn-outline-dark{border:1.5px solid var(--ink);color:var(--ink)}
.photo{position:absolute;background:linear-gradient(150deg,var(--photo-a) 0%,#8a8470 35%,var(--photo-b) 60%,#4c4c48 100%)}

/* header */
.topbar{left:735px;top:0;width:465px;height:34px;background:var(--lime-soft);clip-path:polygon(22px 0,100% 0,100% 100%,48px 100%);display:flex;align-items:center;justify-content:flex-end;gap:34px;padding-right:50px;font-size:12px;font-weight:600;color:var(--ink)}
.topbar span{display:flex;align-items:center;gap:8px}
.brand{display:flex;align-items:center;gap:10px}
.brand-mark{width:20px;height:20px;background:var(--lime)}
.brand-name{font-weight:700;font-size:16px;line-height:1.15;text-transform:uppercase;color:var(--white);letter-spacing:.5px}
.nav{left:527px;top:74px;display:flex;gap:51px;font-size:13px;font-weight:700;text-transform:uppercase}

/* hero */
.badge{left:52px;top:141px;width:354px;height:33px;background:#0f0f0f;border-radius:3px;display:flex;align-items:center;padding-left:22px;gap:8px;font-size:12.5px;font-weight:700;text-transform:uppercase}
.stars{color:#f5c211;letter-spacing:2px;font-size:17px}
.hero-title{left:50px;top:190px;font-size:61px;text-transform:uppercase;line-height:1.1}
.hero-text{left:50px;top:480px;width:400px;font-size:15px;line-height:1.45}

/* stats */
.stat{position:absolute;width:262px;height:116px;background:var(--lime-soft);border-radius:3px;padding:28px 0 0 26px;color:var(--ink)}
.stat-label{font-size:13px;font-weight:600;letter-spacing:1.5px;text-transform:uppercase}
.stat-num{font-family:"Archivo Black",sans-serif;font-size:30px;color:#b3c400;margin-top:10px}
.about-title{left:608px;top:1036px;font-size:60px}
.about-text{left:608px;top:1254px;width:530px;font-size:13.5px;line-height:1.5}

/* services */
.services-band{left:0;top:1486px;width:1200px;height:664px;background:var(--lime);clip-path:polygon(0 0,0 0,1080px 57px,1200px 0,1200px 100%,0 100%)}
.services-title{left:84px;top:1544px;font-size:62px;color:var(--ink)}
.services-sub{left:84px;top:1628px;font-size:13px;font-weight:500;color:var(--ink)}
.service-card{position:absolute;top:1670px;width:333px;height:435px;background:var(--lime-soft);clip-path:polygon(0 0,100% 38px,100% 375px,0 100%);color:var(--ink);padding:72px 30px 0 35px}
.service-card h3{font-size:20px;font-weight:700;text-transform:uppercase;letter-spacing:1px;line-height:1.32}
.service-card p{margin-top:28px;font-size:13.5px;line-height:1.48;width:240px;color:#2f2f2f}
.see-more{position:absolute;left:38px;top:353px;font-family:"Oswald",sans-serif;font-size:14px;display:flex;align-items:center;gap:8px}
.nav-circle{position:absolute;width:29px;height:29px;border-radius:50%;display:flex;align-items:center;justify-content:center}
.dots{position:absolute;display:flex;gap:4px}
.dots i{width:7px;height:7px;border-radius:50%;background:#eeeeee;display:block}

/* why choose */
.section-title{left:0;width:1200px;text-align:center}
.why-card{position:absolute;top:2335px;width:157px;height:185px;background:var(--lime-soft);border-radius:4px;color:var(--ink);padding:32px 0 0 22px}
.why-icon{width:52px;height:52px;background:var(--lime);border-radius:3px;display:flex;align-items:center;justify-content:center}
.why-card p{margin-top:25px;font-size:13px;font-weight:600;line-height:1.5;text-transform:uppercase}
.testimonial{left:259px;top:2690px;width:682px;height:218px;background:#f7f8e6;border-radius:6px;color:var(--ink);padding:38px 60px 0 57px}
.testimonial q{font-size:15px;line-height:1.45;display:block}
.author{position:absolute;right:65px;top:140px;font-size:15px;font-weight:600}
.author small{display:block;font-size:11px;font-weight:400;margin-top:4px}

/* cta */
.cta{left:49px;top:3056px;width:1100px;height:325px;background:var(--bg-deep);border-radius:6px}

/* footer */
.footer{left:0;top:3456px;width:1200px;height:402px;background:var(--footer)}
.footer h4{font-size:20px;font-weight:700}
.footer-list{list-style:none;font-size:15px;color:#dcdcdc}
.footer-list li{height:45px}
.contact-row{position:absolute;left:886px;display:flex;align-items:center;gap:14px;font-size:13px}
.contact-dot{width:32px;height:32px;border-radius:50%;background:var(--lime);display:flex;align-items:center;justify-content:center}
.social{width:26px;height:26px;border-radius:50%;background:var(--white);display:inline-block;margin-right:17px}
</style>
</head>
<body>

<!-- Header -->
<div class="abs topbar">
  <span><svg width="14" height="14" viewBox="0 0 24 24" fill="none" stroke="#1a1a1a" stroke-width="2"><path d="M22 16.9v3a2 2 0 0 1-2.2 2 19.8 19.8 0 0 1-8.6-3.1 19.5 19.5 0 0 1-6-6A19.8 19.8 0 0 1 2.1 4.2 2 2 0 0 1 4.1 2h3a2 2 0 0 1 2 1.7c.1.9.4 1.8.7 2.7a2 2 0 0 1-.5 2.1L8 9.8a16 16 0 0 0 6 6l1.3-1.3a2 2 0 0 1 2.1-.4c.9.3 1.8.6 2.7.7a2 2 0 0 1 1.7 2z"/></svg>+61 8 5550 1942</span>
  <span><svg width="15" height="13" viewBox="0 0 24 20" fill="none" stroke="#1a1a1a" stroke-width="2"><rect x="1" y="1" width="22" height="18" rx="2"/><path d="M1 3l11 8 11-8"/></svg>hello@gullwindstonecut.example</span>
</div>
<div class="abs brand" style="left:52px;top:38px">
  <span class="brand-mark"></span>
  <span class="brand-name">Gullwind Stonecut<br>Earthworks</span>
</div>
<nav class="abs nav"><span>Service</span><span>Projects</span><span>Process</span><span>Safety</span></nav>
<div class="btn btn-lime" style="left:986px;top:59px;width:165px;height:47px">Request Quote</div>

<!-- Hero -->
<div class="photo" role="img" aria-label="Yellow excavator on tracks on a gravel site with forested mountains behind" style="left:435px;top:132px;width:765px;height:512px;clip-path:polygon(172px 0,100% 0,100% 100%,0 100%)"></div>
<div class="abs badge">Trusted by thousands <span class="stars">★★★★★</span></div>
<h1 class="abs display hero-title">Building with<br>precision,<br>safety, and<br>experience.</h1>
<p class="abs hero-text">From Site Preparation To Final Grading, We Deliver Dependable Excavation Solutions For Residential, Commercial, And Industrial Projects.</p>
<div class="btn btn-lime" style="left:50px;top:595px;width:184px;height:47px">Get a free quote</div>
<div class="btn btn-outline" style="left:258px;top:595px;width:147px;height:47px">See projects</div>

<!-- About / stats -->
<div class="photo" role="img" aria-label="Close view of a yellow excavator arm over a gravel bed below snowy mountains" style="left:0;top:697px;width:502px;height:727px;clip-path:polygon(0 0,100% 195px,100% 100%,0 100%)"></div>
<div class="stat" style="left:608px;top:708px"><div class="stat-label">Projects completed</div><div class="stat-num">800+</div></div>
<div class="stat" style="left:887px;top:708px"><div class="stat-label">Years experience</div><div class="stat-num">20+</div></div>
<div class="stat" style="left:608px;top:836px"><div class="stat-label">Machinery units</div><div class="stat-num">30+</div></div>
<div class="stat" style="left:887px;top:836px"><div class="stat-label">Safety rating</div><div class="stat-num">100%</div></div>
<h2 class="abs display about-title">Your Trusted<br>Earthworks<br>Partner</h2>
<svg class="abs" style="left:1000px;top:1102px" width="120" height="124" viewBox="0 0 120 124">
  <circle cx="59" cy="65" r="54" fill="var(--blue)"/>
  <circle cx="70" cy="44" r="36" fill="none" stroke="#fff" stroke-width="2.5"/>
  <path d="M52 44l13 13 24-26" fill="none" stroke="#fff" stroke-width="5" stroke-linecap="round" stroke-linejoin="round"/>
</svg>
<p class="abs about-text">We Are A Professional Excavation &amp; Earthworks Company With Years Of Hands-On Experience In Delivering High-Quality Groundworks. Our Skilled Operators, Modern Machinery, And Commitment To Safety Ensure Every Project Is Completed On Time And To The Highest Standard.</p>
<div class="btn btn-lime" style="left:608px;top:1387px;width:137px;height:47px">Learn more</div>

<!-- Services -->
<div class="abs services-band"></div>
<h2 class="abs display services-title">Our Services</h2>
<p class="abs services-sub">We Use Well-Maintained Machinery And Proven Techniques To Deliver Efficient, Cost-Effective Results.</p>
<div class="btn btn-outline-dark" style="left:956px;top:1597px;width:160px;height:47px">More services</div>

<div class="service-card" style="left:84px">
  <h3>Excavation &amp;<br>Earthmoving</h3>
  <p>We Provide Precise And Efficient Excavation Services Using Modern Machinery. From Small Residential Digs To Large-Scale Earthmoving Projects, We Ensure Accuracy, Safety, And Minimal Site Disruption.</p>
  <div class="see-more">SEE MORE <svg width="14" height="12" viewBox="0 0 14 12" fill="none" stroke="#1a1a1a" stroke-width="1.8"><path d="M1 6h11M7 1l5 5-5 5"/></svg></div>
</div>
<div class="service-card" style="left:433px">
  <h3>Site Preparation &amp;<br>Clearing</h3>
  <p>Our Site Preparation Services Ensure Your Land Is Ready For Construction. This Includes Clearing Vegetation, Removing Debris, And Leveling The Ground To Create A Stable And Compliant Worksite.</p>
  <div class="see-more">SEE MORE <svg width="14" height="12" viewBox="0 0 14 12" fill="none" stroke="#1a1a1a" stroke-width="1.8"><path d="M1 6h11M7 1l5 5-5 5"/></svg></div>
</div>
<div class="service-card" style="left:783px">
  <h3>Trenching &amp;<br>Drainage</h3>
  <p>We Specialize In Trenching For Utilities, Plumbing, And Drainage Systems. Our Team Ensures Correct Depth, Alignment, And Proper Water Flow To Prevent Future Issues.</p>
  <div class="see-more">SEE MORE <svg width="14" height="12" viewBox="0 0 14 12" fill="none" stroke="#1a1a1a" stroke-width="1.8"><path d="M1 6h11M7 1l5 5-5 5"/></svg></div>
</div>
<div class="nav-circle" style="left:49px;top:1866px;background:var(--ink)"><svg width="14" height="12" viewBox="0 0 14 12" fill="none" stroke="#fff" stroke-width="1.8"><path d="M13 6H2M7 1L2 6l5 5"/></svg></div>
<div class="nav-circle" style="left:1122px;top:1866px;background:var(--ink)"><svg width="14" height="12" viewBox="0 0 14 12" fill="none" stroke="#fff" stroke-width="1.8"><path d="M1 6h11M7 1l5 5-5 5"/></svg></div>
<div class="dots" style="left:578px;top:2120px"><i style="background:var(--ink)"></i><i></i><i></i><i></i></div>

<!-- Why choose us -->
<h2 class="abs display section-title" style="top:2228px;font-size:62px">Why Choose Us</h2>
<div class="why-card" style="left:84px"><div class="why-icon"><svg width="26" height="22" viewBox="0 0 26 22" fill="none" stroke="#1a1a1a" stroke-width="2"><rect x="1" y="1" width="24" height="20" rx="2"/><circle cx="8" cy="9" r="3"/><path d="M4 16c1-3 7-3 8 0M15 8h7M15 13h7"/></svg></div><p>Experienced<br>&amp; licensed<br>operators</p></div>
<div class="why-card" style="left:259px"><div class="why-icon"><svg width="28" height="22" viewBox="0 0 28 22" fill="none" stroke="#1a1a1a" stroke-width="2"><rect x="1" y="12" width="16" height="6" rx="3"/><path d="M4 12V6h7l2 6M13 6l8-4 5 8"/><circle cx="5" cy="15" r="1"/><circle cx="13" cy="15" r="1"/></svg></div><p>Modern<br>excavators &amp;<br>equipment</p></div>
<div class="why-card" style="left:434px"><div class="why-icon"><svg width="22" height="24" viewBox="0 0 22 24" fill="none" stroke="#1a1a1a" stroke-width="2"><path d="M11 1l9 4v6c0 6-4 10-9 12-5-2-9-6-9-12V5z"/><path d="M7 12l3 3 5-6"/></svg></div><p>Safety-first<br>approach</p></div>
<div class="why-card" style="left:609px"><div class="why-icon"><svg width="24" height="22" viewBox="0 0 24 22" fill="none" stroke="#1a1a1a" stroke-width="2"><path d="M2 21V7l10-5 10 5v14"/><rect x="7" y="11" width="10" height="10"/><path d="M7 15h10"/></svg></div><p>On-time<br>project<br>delivery</p></div>
<div class="why-card" style="left:784px"><div class="why-icon"><svg width="16" height="26" viewBox="0 0 16 26" fill="none" stroke="#1a1a1a" stroke-width="2"><path d="M8 1v24M14 6c-1-2-3-3-6-3-3 0-6 2-6 5s3 4 6 5 6 2 6 5-3 5-6 5-5-1-6-3"/></svg></div><p>Competitive<br>pricing</p></div>
<div class="why-card" style="left:959px"><div class="why-icon"><svg width="24" height="24" viewBox="0 0 24 24" fill="#1a1a1a"><rect x="3" y="2" width="12" height="21"/><rect x="15" y="9" width="7" height="14"/><g fill="#c5d800"><rect x="5" y="5" width="3" height="3"/><rect x="10" y="5" width="3" height="3"/><rect x="5" y="11" width="3" height="3"/><rect x="10" y="11" width="3" height="3"/><rect x="7" y="18" width="4" height="5"/></g></svg></div><p>Residential &amp;<br>commercial<br>expertise</p></div>

<h2 class="abs display section-title" style="top:2590px;font-size:43px">Client Success Story</h2>
<div class="nav-circle" style="left:206px;top:2784px;background:var(--ink);border:1px solid #444"><svg width="14" height="12" viewBox="0 0 14 12" fill="none" stroke="#c5d800" stroke-width="1.8"><path d="M13 6H2M7 1L2 6l5 5"/></svg></div>
<div class="nav-circle" style="left:964px;top:2784px;background:var(--ink);border:1px solid #444"><svg width="14" height="12" viewBox="0 0 14 12" fill="none" stroke="#fff" stroke-width="1.8"><path d="M1 6h11M7 1l5 5-5 5"/></svg></div>
<div class="abs testimonial">
  <q>“Lorem Ipsum is simply dummy text of the printing and typesetting industry. Lorem Ipsum has been the industry's standard dummy text ever since the 1500s”</q>
  <div class="stars abs" style="left:57px;top:155px">★★★★★</div>
  <div class="author">– Marlon Teale<small>Project owner</small></div>
</div>
<div class="dots" style="left:578px;top:2936px"><i style="background:var(--lime)"></i><i></i><i></i><i></i></div>

<!-- CTA -->
<div class="abs cta"></div>
<h2 class="abs display" style="left:117px;top:3118px;font-size:42px;line-height:1.13">Ready to Start Your<br>Project?</h2>
<p class="abs" style="left:117px;top:3212px;width:400px;font-size:13.5px;line-height:1.5">Get In Touch Today For Reliable Excavation And Earthworks Services You Can Trust.</p>
<div class="btn btn-lime" style="left:118px;top:3291px;width:185px;height:47px">Get a free quote</div>
<div class="btn btn-outline" style="left:327px;top:3291px;width:147px;height:47px">See projects</div>
<div class="photo" role="img" aria-label="Yellow excavator arm resting on a gravel site with snow-capped peaks behind" style="left:701px;top:2906px;width:363px;height:517px;clip-path:polygon(0 105px,100% 0,100% 100%,0 100%)"></div>

<!-- Footer -->
<div class="abs footer"></div>
<h4 class="abs" style="left:794px;top:3484px;font-size:20px;font-weight:700">Subscribe for Newsletter</h4>
<div class="abs" style="left:794px;top:3526px;width:225px;height:39px;background:#fff;border-radius:3px 0 0 3px;color:#333;font-size:13px;display:flex;align-items:center;padding-left:12px">Enter Your Email</div>
<div class="abs" style="left:1019px;top:3526px;width:130px;height:39px;background:var(--lime);border-radius:0 3px 3px 0;color:var(--ink);font-size:13px;font-weight:700;display:flex;align-items:center;justify-content:center">Subscribe</div>

<div class="abs brand" style="left:49px;top:3560px">
  <span class="brand-mark"></span>
  <span class="brand-name">Gullwind Stonecut<br>Earthworks</span>
</div>
<p class="abs" style="left:49px;top:3636px;width:280px;font-size:11px;line-height:1.6;color:#dcdcdc">Lorem Ipsum is simply dummy text of the printing and typesetting industry. Lorem Ipsum has been the industry's standard dummy text ever since the 1500s</p>
<div class="abs" style="left:49px;top:3739px"><span class="social"></span><span class="social"></span><span class="social"></span><span class="social"></span></div>
<p class="abs" style="left:49px;top:3826px;font-size:12.5px">© Company- All Rights Reserved</p>

<div class="abs footer" style="background:none;left:423px;top:3586px;width:auto;height:auto"><h4>Services</h4></div>
<ul class="abs footer-list" style="left:423px;top:3638px"><li>Residential</li><li>Commercial</li><li>Machinery</li><li>Safety</li></ul>
<div class="abs footer" style="background:none;left:592px;top:3586px;width:auto;height:auto"><h4>Company</h4></div>
<ul class="abs footer-list" style="left:592px;top:3638px"><li>About Us</li><li>Why us</li><li>News &amp; press</li><li>Contact</li></ul>
<div class="abs footer" style="background:none;left:886px;top:3586px;width:auto;height:auto"><h4>Contact Us</h4></div>
<div class="contact-row" style="top:3637px"><span class="contact-dot"><svg width="14" height="14" viewBox="0 0 24 24" fill="#1a1a1a"><path d="M22 16.9v3a2 2 0 0 1-2.2 2 19.8 19.8 0 0 1-8.6-3.1 19.5 19.5 0 0 1-6-6A19.8 19.8 0 0 1 2.1 4.2 2 2 0 0 1 4.1 2h3a2 2 0 0 1 2 1.7c.1.9.4 1.8.7 2.7a2 2 0 0 1-.5 2.1L8 9.8a16 16 0 0 0 6 6l1.3-1.3a2 2 0 0 1 2.1-.4c.9.3 1.8.6 2.7.7a2 2 0 0 1 1.7 2z"/></svg></span>+61 8 5550 1942</div>
<div class="contact-row" style="top:3694px"><span class="contact-dot"><svg width="15" height="12" viewBox="0 0 24 20" fill="none" stroke="#1a1a1a" stroke-width="2.4"><rect x="1" y="1" width="22" height="18" rx="2"/><path d="M1 3l11 8 11-8"/></svg></span>hello@gullwindstonecut.example</div>
<div class="contact-row" style="top:3751px"><span class="contact-dot"><svg width="12" height="16" viewBox="0 0 12 16" fill="#1a1a1a"><path d="M6 0a6 6 0 0 0-6 6c0 4.5 6 10 6 10s6-5.5 6-10a6 6 0 0 0-6-6zm0 8.5A2.5 2.5 0 1 1 6 3.5a2.5 2.5 0 0 1 0 5z"/></svg></span>18 Quarry Lane, Perth WA 6000</div>

</body>
</html>
```